Pure Aurelle "polish the glow you hold" The whole body approach to beauty, customized skincare a

I need a stronger logo design than what I have now. I currently have a small med spa in Chicago, IL. I will be expanding my brand to New York City and the Hamptons of NY. The services I provide in Chicago include; advanced medical grade skincare treatments, laser, plastic surgery and nutrition counsel. My concept is personalized skincare. Part of my philosophy is to dedicate a lot of time and make myself always available to my clients questions and concerns. To maintain integrity of the Pure Aurelle Philosophy I do not advertise. Pure Aurelle is an "exclusive skincare club" therefore you must be referred by an existing client or staff member in order to get an appointment. My Chicago clientele consists of young professionals competing with their peers to look their absolute best. The New York and Hamptons business has a completely different structure. It is a Mobile med spa service providing treatments at people's homes. The services provided are advanced skincare, wellness, massage, spray tan, hair and makeup. My vision for the new logo design is to exude an image that is both cutting edge, relevant, sophisticated, sexy and modern (sleek) yet practical and strong. It must be eye catching yet simplistic, aesthetically pleasing to look at and above all must promote EXCLUSIVITY! bellow I have attached my current logo design which is printed using silver and gold foil. The other is the logo on my prescription skincare products. I need to merge the two for the brand to be cohesive. I would like to print my business cards on a mirror like material where you can see your reflection. Front of card: the brand Pure Aurelle across the front and across the bottom will be Chicago. New York. Hamptons Back of card: in a font style like writing "Pure Aurelle is the whole body approach to beauty. customized medical grade skincare. massage. wellness counsel. By appointment only
www.purenaurellecare.example p: (555) 318-2046
I am open to all suggestions to make my brand as strong as possible. Please be creative and relevant. Thank you!

```html
<!DOCTYPE html>
<html lang="en">
<head>
<meta charset="utf-8">
<title>Pure Aurelle Wellness — Business Cards</title>
<link href="https://fonts.googleapis.com/css2?family=Exo+2:wght@400;500;600&display=swap" rel="stylesheet">
<style>
  :root {
    --page: #e9ebec;
    --card: #ffffff;
    --card-shade: #f1f2f2;
    --brand-blue: #0f9be0;
    --brand-green: #3fae49;
    --ink-white: #ffffff;
  }
  * { box-sizing: border-box; margin: 0; padding: 0; }
  html, body {
    width: 1200px; height: 898px; overflow: hidden;
    background: var(--page);
    font-family: "Exo 2", sans-serif;
  }
  .sheet {
    position: relative; width: 1200px; height: 898px;
    display: flex; flex-direction: column; align-items: center; justify-content: center; gap: 44px;
  }
  .card {
    position: relative; width: 640px; height: 366px;
    background: linear-gradient(135deg, var(--card) 0%, var(--card-shade) 100%);
    box-shadow: 0 8px 22px rgba(0,0,0,.18);
    overflow: hidden;
  }

  /* back card */
  .card--back { display: flex; flex-direction: column; align-items: center; justify-content: center; gap: 14px; }
  .mark-ring { width: 110px; height: 110px; border: 6px solid var(--brand-green); border-radius: 50%; }
  .wordmark {
    color: var(--brand-blue); font-weight: 600; font-size: 26px; letter-spacing: .5px;
  }

  /* front card */
  .card--front { display: flex; }
  .edge-stripe {
    width: 14px; height: 100%;
    background: linear-gradient(to bottom, var(--brand-blue) 0 30%, var(--brand-green) 30% 62%, var(--brand-blue) 62% 100%);
  }
  .brand-side {
    flex: 0 0 366px; display: flex; flex-direction: column; align-items: center; justify-content: center; gap: 12px;
  }
  .brand-side .mark-ring { width: 78px; height: 78px; border-width: 4px; }
  .brand-side .wordmark { font-size: 24px; }
  .contact-side {
    flex: 1; background: var(--brand-blue); color: var(--ink-white);
    padding: 26px 22px 24px 16px; text-align: right;
    display: flex; flex-direction: column;
  }
  .person-name { font-size: 19px; font-weight: 500; letter-spacing: 1.5px; text-transform: uppercase; }
  .person-role { font-size: 12px; letter-spacing: 1.2px; text-transform: uppercase; margin-top: 2px; }
  .address { font-size: 14px; line-height: 1.45; margin-top: 32px; }
  .lines { list-style: none; margin-top: 26px; font-size: 12.5px; line-height: 1.95; }
  .lines li { display: flex; justify-content: flex-end; align-items: center; gap: 8px; }
  .lines svg { width: 13px; height: 13px; fill: var(--ink-white); flex: none; }
  .lines .web-group { margin-top: 10px; }
</style>
</head>
<body>
<main class="sheet">

  <section class="card card--back" aria-label="Card back">
    <div class="mark-ring"></div>
    <div class="wordmark">Pure Aurelle Wellness</div>
  </section>

  <section class="card card--front" aria-label="Card front">
    <div class="edge-stripe"></div>
    <div class="brand-side">
      <div class="mark-ring"></div>
      <div class="wordmark">Pure Aurelle Wellness</div>
    </div>
    <div class="contact-side">
      <div class="person-name">Dana Merrow</div>
      <div class="person-role">General Manager</div>
      <div class="address">42 Harbor Lane,<br>Suite 3 East</div>
      <ul class="lines">
        <li>555 014 2290
          <svg viewBox="0 0 16 16"><path d="M3 1l3 0 1 4-2 1.5c1 2 2.5 3.5 4.5 4.5L11 9l4 1v3c0 1-1 2-2 2C7 15 1 9 1 3c0-1 1-2 2-2z"/></svg></li>
        <li>555 014 2291
          <svg viewBox="0 0 16 16"><path d="M4 0h8a1 1 0 0 1 1 1v14a1 1 0 0 1-1 1H4a1 1 0 0 1-1-1V1a1 1 0 0 1 1-1zm1 2v10h6V2zm3 11a1 1 0 1 0 0 2 1 1 0 0 0 0-2z"/></svg></li>
        <li>555 014 2292
          <svg viewBox="0 0 16 16"><path d="M4 0h7l2 2v4h1a2 2 0 0 1 2 2v5h-3v3H3v-3H0V8a2 2 0 0 1 2-2h2zm1 1v5h7V3h-2V1zM4 11v4h8v-4z"/></svg></li>
        <li class="web-group">hello@purenaurellecare.example
          <svg viewBox="0 0 16 16"><path d="M0 3h16v10H0zm1 1v.5l7 5 7-5V4zm0 2v6h14V6l-7 5z"/></svg></li>
        <li>www.purenaurellecare.example
          <svg viewBox="0 0 16 16"><path d="M8 0a8 8 0 1 0 0 16A8 8 0 0 0 8 0zm-1 1.1C5.6 2.5 4.9 4.6 4.8 7.5H1.1A7 7 0 0 1 7 1.1zm2 0a7 7 0 0 1 5.9 6.4h-3.7c-.1-2.9-.8-5-2.2-6.4zM8 1.5c1.3 1.4 2 3.3 2.2 6H5.8c.2-2.7.9-4.6 2.2-6zM1.1 8.5h3.7c.1 2.9.8 5 2.2 6.4A7 7 0 0 1 1.1 8.5zm4.7 0h4.4c-.2 2.7-.9 4.6-2.2 6-1.3-1.4-2-3.3-2.2-6zm5.4 0h3.7A7 7 0 0 1 9 14.9c1.4-1.4 2.1-3.5 2.2-6.4z"/></svg></li>
      </ul>
    </div>
  </section>

</main>
</body>
</html>
```